Website for Excavator and Earthworks Company

We require a modern, sleek and practical website for our newly created earthworks/excavator business in Perth, Western Australia called Gullwind Stonecut Earthworks.

The website should have a modern, cutting edge feel but only needs to be relatively simplistic in it's layout and eventual functionality.

Some pages it should have would be Home, About, Projects and Contact Us.

Number of Pages Required

1 page

```html
<!DOCTYPE html>
<html lang="en">
<head>
<meta charset="utf-8">
<title>Gullwind Stonecut Earthworks</title>
<link rel="stylesheet" href="https://fonts.googleapis.com/css2?family=Poppins:wght@300;400;500;600&display=swap">
<style>
:root{
  --lime:#c6dc00;
  --ink:#111111;
  --black:#000000;
  --muted:#8a8a8a;
  --paper:#ffffff;
  --canvas:#f3f3f3;
  --soft:#f5f5f5;
  --line:#cfcfcf;
}
*{margin:0;padding:0;box-sizing:border-box}
html,body{width:1200px;height:1200px;overflow:hidden;background:var(--canvas);font-family:"Poppins",sans-serif;color:var(--ink)}
.page{position:absolute;left:320px;top:0;width:560px;height:1200px;background:var(--paper);overflow:hidden;box-shadow:0 0 18px rgba(0,0,0,.12)}
.abs{position:absolute}
.header{left:0;top:0;width:560px;height:41px}
.brand{left:70px;top:13px;display:flex;align-items:center;gap:6px;font-size:10px;font-weight:600;color:var(--ink)}
.brand .mark{width:12px;height:12px;background:var(--lime)}
.nav{right:70px;top:17px;display:flex;gap:14px;font-size:4.5px;font-weight:600;letter-spacing:.3px}
.nav .active{color:var(--lime)}
.hero-photo{left:0;top:41px;width:560px;height:233px;background:linear-gradient(180deg,#a8b7c4 0%,#8c9a7a 22%,#7a4a2c 45%,#6b3a22 100%);clip-path:polygon(0 0,100% 0,100% 100%,62px 100%,0 75%)}
.hero-card{left:256px;top:156px;width:234px;height:147px;background:var(--black);color:#fff;padding:18px 18px;clip-path:polygon(0 0,206px 0,100% 24px,100% 100%,0 100%)}
.hero-card h1{font-size:10.5px;font-weight:500;line-height:16px;letter-spacing:.6px;text-transform:uppercase}
.hero-card h1 em{font-style:normal;color:var(--lime)}
.hero-card p{margin-top:9px;font-size:5.5px;line-height:10px;font-weight:300}
.btn{display:inline-flex;align-items:center;gap:6px;border:1px solid var(--lime);color:#fff;font-size:5.5px;padding:4px 7px;margin-top:8px}
.btn svg{width:5px;height:5px}
.bar{width:59px;height:3px;background:var(--lime)}
.h2{font-size:12.5px;font-weight:500;line-height:16px}
.body{font-size:5.2px;line-height:9.5px;color:var(--muted)}
.about-photo{left:70px;top:422px;width:209px;height:210px;background:linear-gradient(160deg,#5f8fc9 0%,#8aa77a 30%,#a8793c 60%,#c7a56b 100%);clip-path:polygon(0 0,100% 0,100% 100%,44px 100%,0 162px)}
.sub{font-size:6.5px;font-weight:600;color:var(--ink)}
.values li{list-style:none;display:flex;align-items:center;gap:5px;font-size:5.2px;line-height:9.5px;color:var(--muted)}
.values li::before{content:"";width:4px;height:4px;border-radius:50%;border:1px solid var(--lime)}
.projects{left:0;top:660px;width:560px;height:268px;background:var(--soft)}
.project-photo{width:158px;height:116px;background:linear-gradient(170deg,#7fb0d8 0%,#d4b25d 25%,#c79a44 60%,#a77e3a 100%);clip-path:polygon(0 0,100% 0,100% 78%,132px 100%,0 100%)}
.card-title{font-size:6.5px;font-weight:600;margin-top:12px}
.card-text{font-size:5px;color:var(--muted);margin-top:6px}
.arrow{width:14px;height:10px}
.contact{left:0;top:928px;width:560px;height:272px;background:linear-gradient(180deg,#3a3a3a 0%,#1e1e1e 55%,#0d0d0d 100%);color:#fff}
.contact .body{color:#bdbdbd}
.info{font-size:5.2px;display:flex;align-items:center;gap:6px;color:#e5e5e5;line-height:12px}
.info svg{width:6px;height:6px}
.social{display:flex;gap:8px}
.social span{width:7px;height:7px;border-radius:50%;background:#e5e5e5}
.form{left:280px;top:29px;width:210px;height:203px;background:var(--paper);color:var(--ink);padding:20px 20px;clip-path:polygon(0 0,100% 0,100% 100%,44px 100%,0 174px)}
.form h3{font-size:6.5px;font-weight:600}
.form p{font-size:5px;color:var(--muted);line-height:9px;margin-top:7px}
.field{border:1px solid var(--line);height:14px;margin-top:7px;font-size:4.5px;color:var(--muted);padding:3px 6px}
.field.area{height:44px}
.submit{position:absolute;right:20px;bottom:16px;background:var(--black);color:#fff;font-size:5.5px;padding:4px 9px;display:flex;gap:6px;align-items:center}
.submit svg{width:5px;height:5px}
.copy{left:70px;top:252px;font-size:4.5px;color:#e5e5e5}
.copy em{font-style:normal;color:var(--lime)}
</style>
</head>
<body>
<main class="page">
  <header class="abs header">
    <div class="abs brand"><span class="mark"></span>Gullwind Stonecut Earthworks</div>
    <nav class="abs nav"><span class="active">HOME</span><span>ABOUT</span><span>PROJECTS</span><span>CONTACT</span></nav>
  </header>

  <div class="abs hero-photo" role="img" aria-label="Green and grey excavator working on a red-earth construction site under a cloudy sky"></div>
  <section class="abs hero-card">
    <h1>Welcome to <em>Australia’s<br>trusted partner</em> in earthworks<br>and excavation</h1>
    <p>We combine cutting-edge technology with years of expertise to deliver efficient, sustainable, and reliable solutions for construction and land development projects.</p>
    <span class="btn">Let’s get in touch <svg viewBox="0 0 10 10"><path d="M3 1l4 4-4 4" fill="none" stroke="#c6dc00" stroke-width="1.6"/></svg></span>
  </section>

  <div class="abs bar" style="left:70px;top:303px"></div>
  <h2 class="abs h2" style="left:70px;top:316px">Leading Earth Movers in<br>Western Australia</h2>
  <p class="abs body" style="left:70px;top:357px;width:255px">Lorem ipsum dolor sit amet, consectetur adipiscing elit. Duis semper, neque at sollicitudin cursus, elit lectus hendrerit quam, sit amet gravida dui nisl vitae massa. Vivamus scelerisque imperdiet dui sed porttitor. Aenean id libero aliquet, mollis nisi vel, egestas risus. Etiam sed cursus erat.</p>

  <div class="abs about-photo" role="img" aria-label="Yellow wheel loader beside a gravel stockpile at sunset with trees behind"></div>
  <div class="abs bar" style="left:309px;top:443px;width:30px"></div>
  <h2 class="abs h2" style="left:309px;top:452px">About Us</h2>
  <p class="abs body" style="left:309px;top:473px;width:185px">At Gullwind Stonecut, we pride ourselves on precision, professionalism, and innovation. Our team of experienced operators and engineers ensures every project is completed to the highest standard.</p>
  <div class="abs sub" style="left:309px;top:508px">Our Values:</div>
  <ul class="abs values" style="left:309px;top:521px">
    <li>Integrity and transparency</li>
    <li>Environmental responsibility</li>
    <li>Client-focused service</li>
  </ul>
  <div class="abs sub" style="left:309px;top:563px">Our Mission:</div>
  <p class="abs body" style="left:309px;top:576px;width:185px">To reshape landscapes responsibly, providing earthworks solutions that support Australia’s growing infrastructure needs.</p>

  <section class="abs projects">
    <div class="abs bar" style="left:265px;top:27px;width:30px"></div>
    <h2 class="abs h2" style="left:0;top:38px;width:560px;text-align:center">Recent Projects</h2>
    <p class="abs body" style="left:0;top:56px;width:560px;text-align:center;font-size:4.5px">Explore some of our recent work</p>
    <svg class="abs arrow" style="left:70px;top:114px" viewBox="0 0 14 10"><path d="M13 5H1M5 1L1 5l4 4" fill="none" stroke="#9a9a9a" stroke-width="1"/></svg>
    <div class="abs" style="left:108px;top:78px;width:158px">
      <div class="project-photo" role="img" aria-label="Wheel loader working in a sandy quarry"></div>
      <div class="card-title">Infrastructure</div>
      <div class="card-text">Roadworks, drainage, and land reclamation.</div>
    </div>
    <div class="abs" style="left:294px;top:78px;width:158px">
      <div class="project-photo" role="img" aria-label="Wheel loader moving sand in an open quarry"></div>
      <div class="card-title">Commercial Projects</div>
      <div class="card-text">Large-scale earthmoving for industrial facilities.</div>
    </div>
    <svg class="abs arrow" style="left:476px;top:114px" viewBox="0 0 14 10"><path d="M1 5h12M9 1l4 4-4 4" fill="none" stroke="#444" stroke-width="1"/></svg>
  </section>

  <section class="abs contact" role="img" aria-label="Dark monochrome backdrop of trees and earthmoving machinery">
    <div class="abs bar" style="left:70px;top:37px;width:30px"></div>
    <h2 class="abs h2" style="left:70px;top:46px;color:#fff">Contact Us</h2>
    <p class="abs body" style="left:70px;top:67px;width:150px">We’d love to hear from you! Reach out to discuss your next project.</p>
    <div class="abs sub" style="left:70px;top:95px;color:#fff">Let’s get in touch</div>
    <div class="abs" style="left:70px;top:106px">
      <div class="info"><svg viewBox="0 0 10 10"><path d="M2 1l2 2-1 1.5c.8 1.5 1.5 2.2 3 3L7.5 6l2 2-1.5 1.5C4.5 9 1 5.5.5 2.5z" fill="#c6dc00"/></svg>+61 (08) 5550 1420</div>
      <div class="info"><svg viewBox="0 0 10 10"><path d="M1 5l8-4-3 8-1.5-3z" fill="#c6dc00"/></svg>hello@gullwindstonecut.com.au</div>
      <div class="info"><svg viewBox="0 0 10 10"><path d="M5 10C2 6 1.5 5 1.5 3.5a3.5 3.5 0 017 0C8.5 5 8 6 5 10z" fill="#c6dc00"/><circle cx="5" cy="3.6" r="1.3" fill="#1e1e1e"/></svg>14 Quarry Lane, Perth, WA 6016</div>
    </div>
    <div class="abs sub" style="left:70px;top:158px;color:#fff">We’re social</div>
    <div class="abs social" style="left:70px;top:172px"><span></span><span></span><span></span></div>

    <form class="abs form">
      <h3>Fill the contact form</h3>
      <p>We’d love to hear from you! We will reach out to discuss your next project.</p>
      <div class="field">Your Name *</div>
      <div class="field">Your Email *</div>
      <div class="field">Your Phone</div>
      <div class="field area">Your Message</div>
      <span class="submit">Submit <svg viewBox="0 0 10 10"><path d="M3 1l4 4-4 4" fill="none" stroke="#c6dc00" stroke-width="1.6"/></svg></span>
    </form>

    <div class="abs copy">© 2025 <em>Gullwind Stonecut Earthworks</em>. All Rights Reserved.</div>
  </section>
</main>
</body>
</html>
```